New modern business card design

To design a brand new business card that's clean & modern in terms of layout.
I have attached our company logo and also basic information regarding what is needed on the card that also needs to be editable.

Target Market(s)

motor trade

Contact Information for Business Card

logo, name, title, tel, mob, email, address, www, all information is in the word.doc file

Requirements
Must have
• white background
Nice to have
• Nice clean font

```html
<!DOCTYPE html>
<html lang="en">
<head>
<meta charset="utf-8">
<title>Boltline Ltd — Business Card</title>
<link href="https://fonts.googleapis.com/css2?family=Lexend:wght@500;600&display=swap" rel="stylesheet">
<style>
  :root {
    --stage: #dcd9d9;
    --card: #f7f7f7;
    --brand-blue: #2672bd;
    --band-blue: #4f8fca;
    --hex-blue: #8db4db;
    --ink: #2a2626;
    --white: #ffffff;
  }
  * { margin: 0; padding: 0; box-sizing: border-box; }
  html, body { width: 1200px; height: 1200px; overflow: hidden; }
  body {
    background: var(--stage);
    font-family: "Lexend", sans-serif;
    color: var(--ink);
    position: relative;
  }
  .card {
    position: absolute;
    left: 179px;
    width: 840px;
    height: 480px;
    overflow: hidden;
    box-shadow: 2px 3px 4px rgba(0,0,0,0.45);
  }
  .card--front { top: 122px; }
  .card--back { top: 618px; }
  .card__texture {
    position: absolute; inset: 0;
    background: linear-gradient(135deg, #eeeeee 0%, #fbfbfb 35%, #ececec 60%, #f9f9f9 100%);
  }
  .band {
    position: absolute;
    left: 47px;
    width: 746px;
    height: 47px;
    background: var(--band-blue);
    color: var(--white);
    font-weight: 600;
    font-size: 25px;
    display: flex; align-items: center; justify-content: center;
    letter-spacing: -0.2px;
  }
  .band--bottom { top: 433px; }
  .band--top { top: 0; }

  .hex-badge { position: absolute; left: 30px; top: 40px; width: 376px; height: 380px; }
  .hex-badge__name {
    position: absolute; left: 30px; top: 40px; width: 376px; height: 380px;
    display: flex; align-items: center; justify-content: center;
    color: var(--white); font-weight: 600; font-size: 30px; letter-spacing: 1px;
  }

  .person-name {
    position: absolute; left: 444px; top: 70px;
    font-weight: 600; font-size: 38px; letter-spacing: 0.5px; line-height: 1;
  }
  .name-marker {
    position: absolute; left: 793px; top: 51px; width: 47px; height: 48px;
    background: var(--brand-blue);
  }
  .divider {
    position: absolute; left: 440px; top: 101px; width: 4px; height: 293px;
    background: var(--brand-blue);
  }
  .contact-list { position: absolute; left: 472px; top: 126px; list-style: none; }
  .contact-item {
    display: flex; align-items: flex-start;
    font-weight: 500; font-size: 21px; line-height: 26px;
  }
  .contact-item + .contact-item { margin-top: 16px; }
  .contact-item:nth-child(3), .contact-item:nth-child(4) { margin-top: 15px; }
  .contact-icon { width: 34px; height: 34px; flex: none; margin-right: 19px; margin-top: -4px; }

  .wordmark {
    position: absolute; left: 0; right: 0; top: 230px;
    display: flex; align-items: center; justify-content: center; gap: 18px;
  }
  .wordmark__square { width: 42px; height: 42px; background: var(--brand-blue); }
  .wordmark__name {
    color: var(--brand-blue); font-weight: 600; font-size: 60px; letter-spacing: 2px; line-height: 1;
  }
</style>
</head>
<body>

<section class="card card--front">
  <div class="card__texture" role="img" aria-label="Soft faceted light grey background texture"></div>

  <svg class="hex-badge" viewBox="0 0 376 380" aria-hidden="true">
    <polygon points="188,6 349,99 349,281 188,374 27,281 27,99" fill="var(--hex-blue)" opacity="0.85"/>
    <polygon points="188,26 332,109 332,271 188,354 44,271 44,109" fill="none" stroke="var(--white)" stroke-width="3"/>
  </svg>
  <div class="hex-badge__name">BOLTLINE LTD</div>

  <h1 class="person-name">DANIEL MARSH</h1>
  <div class="name-marker"></div>
  <div class="divider"></div>

  <ul class="contact-list">
    <li class="contact-item">
      <svg class="contact-icon" viewBox="0 0 34 34" aria-hidden="true"><circle cx="17" cy="17" r="17" fill="var(--brand-blue)"/><circle cx="17" cy="13" r="4.5" fill="#fff"/><path d="M9 25c0-5 3.5-7 8-7s8 2 8 7z" fill="#fff"/></svg>
      <span>General Manager</span>
    </li>
    <li class="contact-item">
      <svg class="contact-icon" viewBox="0 0 34 34" aria-hidden="true"><circle cx="17" cy="17" r="17" fill="var(--brand-blue)"/><rect x="9" y="9" width="16" height="16" rx="3" fill="none" stroke="#fff" stroke-width="2"/><path d="M13 12l2 0 1 3-1.5 1a6 6 0 0 0 3 3l1-1.5 3 1v2a2 2 0 0 1-2 1c-4 0-8-4-8-8a2 2 0 0 1 1.5-1.5z" fill="#fff"/></svg>
      <span>0161 555 0192</span>
    </li>
    <li class="contact-item">
      <svg class="contact-icon" viewBox="0 0 34 34" aria-hidden="true"><circle cx="17" cy="17" r="17" fill="var(--brand-blue)"/><rect x="12" y="8" width="10" height="18" rx="2" fill="none" stroke="#fff" stroke-width="2"/><circle cx="17" cy="22.5" r="1.2" fill="#fff"/></svg>
      <span>07700 900 418</span>
    </li>
    <li class="contact-item">
      <svg class="contact-icon" viewBox="0 0 34 34" aria-hidden="true"><circle cx="17" cy="17" r="17" fill="var(--brand-blue)"/><rect x="9" y="11" width="16" height="12" rx="1.5" fill="#fff"/><path d="M9.5 12l7.5 6 7.5-6" fill="none" stroke="var(--brand-blue)" stroke-width="1.8"/></svg>
      <span>dmarsh@boltline-ltd.co.uk</span>
    </li>
    <li class="contact-item">
      <svg class="contact-icon" viewBox="0 0 34 34" aria-hidden="true"><circle cx="17" cy="17" r="17" fill="var(--brand-blue)"/><path d="M17 24s-5-5.5-5-9a5 5 0 0 1 10 0c0 3.5-5 9-5 9z" fill="none" stroke="#fff" stroke-width="2"/><circle cx="17" cy="14.5" r="1.8" fill="#fff"/><ellipse cx="17" cy="25.5" rx="4" ry="1.2" fill="none" stroke="#fff" stroke-width="1.2"/></svg>
      <span>Foundry Lane<br>Eastwick, Northby<br>NB4 2QT</span>
    </li>
  </ul>

  <div class="band band--bottom">www.boltline-ltd.co.uk</div>
</section>

<section class="card card--back">
  <div class="card__texture" role="img" aria-label="Soft faceted light grey background texture"></div>
  <div class="band band--top"></div>
  <div class="wordmark">
    <span class="wordmark__square"></span>
    <span class="wordmark__name">BOLTLINE LTD</span>
  </div>
  <div class="band band--bottom">www.boltline-ltd.co.uk</div>
</section>

</body>
</html>
```